Celebrate February in The Smokies at Maple Hollow Splashpark Lodge

Create something similar to the attached design - can very and be creative but the overall concept is one I would like to recreate
Celebrate February in The Smokies
Maple Hollow logo (at top)
Romantic Rooms, Family Suites, Free Buffet Breakfast included, Indoor Pool and Parkway Convenience
Low Rates!

866.214.5093 MapleHollowLodge.example/

I have attached logos and pictures to use

Target Market(s)

Email customers to entice them to come to the smokies in February ..

Industry/Entity Type

Hospitality

Requirements
Must have
• phone number 866.214.5093
• website MapleHollowLodge.example/
Nice to have
• a romantic feel but not to much so .. families and couples can both enjoy the area in february

```html
<!DOCTYPE html>
<html lang="en">
<head>
<meta charset="utf-8">
<title>Celebrate February in The Smokies – Maple Hollow Splashpark Lodge</title>
<link rel="stylesheet" href="https://fonts.googleapis.com/css2?family=Rubik:wght@300;400;500&family=Poppins:wght@400&display=swap">
<style>
  :root {
    --sky: #41b1f5;
    --navy: #14168a;
    --link-navy: #0a0a7a;
    --pill-green: #0f6310;
    --white: #ffffff;
    --ink: #111111;
    --footer-bg: #e5eef7;
    --footer-ink: #222222;
    --social-ring: #3f5fa8;
    --photo-light: #5e3f2b;
    --photo-dark: #2b1e17;
  }
  * { margin: 0; padding: 0; box-sizing: border-box; }
  html, body { width: 1200px; height: 2190px; overflow: hidden; background: var(--white); }
  body { position: relative; font-family: "Rubik", Arial, sans-serif; color: var(--ink); }

  .hero { position: absolute; left: 0; top: 0; width: 1200px; height: 1095px; overflow: hidden; }
  .hero-photo {
    position: absolute; inset: 0;
    background: linear-gradient(135deg, var(--photo-light) 0%, var(--photo-dark) 100%);
  }
  .hero-waves { position: absolute; inset: 0; width: 1200px; height: 1095px; }

  .brand {
    position: absolute; right: 30px; top: 40px;
    display: flex; align-items: center; gap: 16px;
  }
  .brand-dot { width: 110px; height: 110px; border-radius: 50%; background: var(--sky); flex: none; }
  .brand-name {
    font-family: "Rubik", Arial, sans-serif; font-weight: 500; color: var(--navy);
    font-size: 42px; line-height: 1.1;
  }

  .headline {
    position: absolute; left: 584px; top: 490px;
    color: var(--white); font-weight: 300; line-height: 1.2;
  }
  .headline .line-one { display: block; font-size: 66px; }
  .headline .line-two { display: block; font-size: 80px; font-weight: 400; margin-top: 2px; }

  .phone-pill {
    position: absolute; width: 414px; height: 90px; border-radius: 45px;
    background: var(--pill-green); color: var(--white);
    display: flex; align-items: center; gap: 30px; padding-left: 12px;
    font-size: 45px; font-weight: 400; text-decoration: none;
  }
  .phone-pill .phone-icon {
    width: 70px; height: 70px; border-radius: 50%; background: var(--white);
    display: flex; align-items: center; justify-content: center; flex: none;
  }
  .phone-pill.hero-call { left: 586px; top: 701px; }
  .phone-pill.body-call { left: 393px; top: 1481px; }

  .offer {
    position: absolute; left: 0; top: 1160px; width: 1200px;
    text-align: center; font-size: 49px; font-weight: 300; line-height: 87px;
  }
  .site-link {
    position: absolute; left: 0; top: 1632px; width: 1200px; text-align: center;
    font-family: Arial, Helvetica, sans-serif; font-size: 45px;
    color: var(--link-navy); text-decoration: underline; text-underline-offset: 8px;
  }

  .footer {
    position: absolute; left: 0; top: 1805px; width: 1200px; height: 385px;
    background: var(--footer-bg); font-family: "Poppins", Arial, sans-serif; color: var(--footer-ink);
  }
  .copyright { position: absolute; left: 0; top: 87px; width: 1200px; text-align: center; font-size: 27px; }
  .ref-code { position: absolute; right: 38px; top: 100px; font-size: 22px; }
  .footer-links { position: absolute; left: 0; top: 152px; width: 1200px; text-align: center; font-size: 27px; }
  .social { position: absolute; left: 463px; top: 242px; display: flex; gap: 11px; }
  .social span { width: 61px; height: 61px; border-radius: 50%; border: 3px solid var(--social-ring); }
</style>
</head>
<body>
  <section class="hero">
    <div class="hero-photo" role="img" aria-label="Photo: a couple in winter coats on a warmly lit evening street"></div>
    <svg class="hero-waves" viewBox="0 0 1200 1095" aria-hidden="true">
      <path d="M0 0 H1200 V275 C900 260 700 130 400 50 C250 15 100 40 0 80 Z" fill="var(--sky)"/>
      <path d="M0 0 H1200 V250 C920 230 720 110 420 30 C270 -5 100 15 0 40 Z" fill="var(--white)"/>
      <path d="M0 1000 C200 955 450 950 700 1010 C900 1060 1100 1070 1200 1015 V1095 H0 Z" fill="var(--sky)"/>
      <path d="M0 1095 V1085 C250 995 500 1005 750 1055 C950 1090 1100 1080 1200 1040 V1095 Z" fill="var(--white)"/>
    </svg>

    <div class="brand">
      <span class="brand-dot"></span>
      <span class="brand-name">Maple Hollow<br>Splashpark Lodge</span>
    </div>

    <h1 class="headline">
      <span class="line-one">Celebrate February</span>
      <span class="line-two">in The Smokies</span>
    </h1>

    <a class="phone-pill hero-call" href="tel:8662145093">
      <span class="phone-icon">
        <svg width="38" height="38" viewBox="0 0 24 24" aria-hidden="true"><path fill="var(--pill-green)" d="M6.6 10.8a15.1 15.1 0 0 0 6.6 6.6l2.2-2.2a1 1 0 0 1 1-.25 11.4 11.4 0 0 0 3.6.57 1 1 0 0 1 1 1V20a1 1 0 0 1-1 1A17 17 0 0 1 3 4a1 1 0 0 1 1-1h3.5a1 1 0 0 1 1 1c0 1.25.2 2.45.57 3.6a1 1 0 0 1-.25 1z"/></svg>
      </span>
      866.214.5093
    </a>
  </section>

  <p class="offer">Romantic Rooms, Family Suites, Free Buffet<br>Breakfast included, Indoor Pool and Parkway<br>Convenience Low Rates!</p>

  <a class="phone-pill body-call" href="tel:8662145093">
    <span class="phone-icon">
      <svg width="38" height="38" viewBox="0 0 24 24" aria-hidden="true"><path fill="var(--pill-green)" d="M6.6 10.8a15.1 15.1 0 0 0 6.6 6.6l2.2-2.2a1 1 0 0 1 1-.25 11.4 11.4 0 0 0 3.6.57 1 1 0 0 1 1 1V20a1 1 0 0 1-1 1A17 17 0 0 1 3 4a1 1 0 0 1 1-1h3.5a1 1 0 0 1 1 1c0 1.25.2 2.45.57 3.6a1 1 0 0 1-.25 1z"/></svg>
    </span>
    866.214.5093
  </a>

  <a class="site-link" href="https://MapleHollowLodge.example/">www.MapleHollowLodge.example</a>

  <footer class="footer">
    <p class="copyright">Copyright © Maple Hollow Splashpark Lodge. All Rights Reserved.</p>
    <span class="ref-code">c7</span>
    <p class="footer-links">About Us | Contact Us | Terms of Use | Privacy Policy</p>
    <div class="social" aria-label="Social links">
      <span></span><span></span><span></span><span></span>
    </div>
  </footer>
</body>
</html>
```